Graphics for Book geared to Professionals

We need the attached graphics professional recreated for our book. The book will be in black and white so it will need to be grey scale. Please see the best practices for graphics from our publisher Harlow.
The power point attached has several graphics that we need professional illustrated. The graphics in a excel format simply need to be transposed professionally (slides 8-14). The graphs in the other slides need to have some design put behind them. These make the general look and feel somewhat consistent. If you have any questions, you can email me at marcus.thorne@velquist.com.

Target Market(s)

Professionals, Business Analyst

Industry/Entity Type

It Professional

Font styles to use
Other font styles liked:
• Calibre

Requirements
Must have
• Professional looks and feel

```html
<!DOCTYPE html>
<html lang="en">
<head>
<meta charset="utf-8">
<title>Analytical Cycle</title>
<link rel="stylesheet" href="https://fonts.googleapis.com/css2?family=Raleway:wght@300;400;700;800&display=swap">
<style>
  :root {
    --ink: #1f2124;
    --slate: #4d535b;
    --arrow: #575d65;
    --mid: #8a8f96;
    --light: #bfc3c8;
    --faint: #e9eaec;
    --paper: #ffffff;
  }
  html, body {
    margin: 0;
    padding: 0;
    overflow: hidden;
    background: var(--paper);
  }
  .canvas {
    position: relative;
    width: 1200px;
    height: 1020px;
    overflow: hidden;
    background: var(--paper);
    font-family: "Raleway", "Helvetica Neue", Arial, sans-serif;
    color: var(--ink);
  }
  .cycle-art {
    position: absolute;
    inset: 0;
    width: 1200px;
    height: 1020px;
  }
  .title {
    position: absolute;
    left: 146px;
    top: 18px;
    margin: 0;
    font-size: 52px;
    font-weight: 800;
    letter-spacing: -0.5px;
    color: var(--ink);
  }
  .hub-label {
    position: absolute;
    left: 523px;
    top: 545px;
    width: 200px;
    text-align: center;
    font-size: 46px;
    font-weight: 400;
    margin: 0;
  }
  .stage {
    position: absolute;
    margin: 0;
    width: 480px;
    text-align: center;
    font-size: 36px;
    font-weight: 300;
    line-height: 60px;
    letter-spacing: 0.3px;
  }
  .stage .key {
    font-weight: 700;
    text-decoration: underline;
    text-decoration-thickness: 2px;
    text-underline-offset: 7px;
  }
  .stage--measure { left: 38px;  top: 257px; }
  .stage--inform  { left: 727px; top: 288px; }
  .stage--diagnose{ left: 727px; top: 736px; }
  .stage--action  { left: 32px;  top: 728px; }
</style>
</head>
<body>
<div class="canvas">
  <svg class="cycle-art" viewBox="0 0 1000 850" xmlns="http://www.w3.org/2000/svg">
    <!-- faint stage icons -->
    <rect role="img" aria-label="Faint set-square and ruler icon" x="150" y="305" width="80" height="60" rx="6" fill="var(--faint)"/>
    <rect role="img" aria-label="Faint clipboard icon" x="702" y="290" width="48" height="62" rx="5" fill="var(--faint)"/>
    <rect role="img" aria-label="Faint stethoscope icon" x="680" y="615" width="40" height="70" rx="18" fill="var(--faint)"/>
    <rect role="img" aria-label="Faint gavel icon" x="215" y="690" width="115" height="70" rx="8" fill="var(--faint)"/>

    <!-- hub -->
    <circle class="hub-ring" cx="519" cy="478" r="86" fill="none" stroke="var(--faint)" stroke-width="3"/>

    <!-- growth bar icon -->
    <g class="icon-growth" fill="var(--slate)">
      <rect x="413" y="397" width="9" height="33"/>
      <rect x="427" y="389" width="9" height="41"/>
      <rect x="441" y="403" width="9" height="27"/>
      <rect x="455" y="393" width="9" height="37"/>
      <polyline points="410,392 428,378 444,392 472,372" fill="none" stroke="var(--slate)" stroke-width="5"/>
      <polygon points="462,368 476,368 476,382"/>
    </g>
    <!-- area chart icon -->
    <g class="icon-area">
      <polygon points="558,420 576,392 590,402 608,376 620,384 638,356 638,428 558,428" fill="var(--light)"/>
      <polygon points="552,428 570,400 586,410 604,384 618,392 636,366 636,428" fill="var(--slate)"/>
    </g>
    <!-- bar chart icon -->
    <g class="icon-bars">
      <rect x="392" y="560" width="6" height="40" fill="var(--light)"/>
      <rect x="403" y="546" width="6" height="54" fill="var(--light)"/>
      <rect x="414" y="555" width="6" height="45" fill="var(--mid)"/>
      <rect x="425" y="538" width="6" height="62" fill="var(--light)"/>
      <rect x="436" y="545" width="6" height="55" fill="var(--mid)"/>
      <rect x="447" y="532" width="6" height="68" fill="var(--light)"/>
      <rect x="458" y="548" width="6" height="52" fill="var(--mid)"/>
      <rect x="466" y="525" width="7" height="75" fill="var(--slate)"/>
      <rect x="478" y="540" width="6" height="60" fill="var(--light)"/>
      <rect x="489" y="568" width="6" height="32" fill="var(--light)"/>
    </g>
    <!-- presentation board icon -->
    <g class="icon-board" fill="var(--slate)">
      <rect x="572" y="537" width="62" height="6"/>
      <rect x="576" y="543" width="54" height="38" fill="none" stroke="var(--slate)" stroke-width="4"/>
      <path d="M594,552 A10,10 0 1 0 604,562 L594,562 Z"/>
      <rect x="608" y="553" width="14" height="3"/>
      <rect x="608" y="560" width="14" height="3"/>
      <rect x="608" y="567" width="14" height="3"/>
      <rect x="601" y="581" width="4" height="18"/>
      <polygon points="590,605 601,586 605,586 594,605"/>
      <polygon points="616,605 605,586 601,586 612,605"/>
    </g>

    <!-- cycle arrows -->
    <g class="cycle-arrows" fill="var(--arrow)" stroke="none">
      <path d="M460,208 Q500,190 545,195" fill="none" stroke="var(--arrow)" stroke-width="8" stroke-linecap="round"/>
      <path d="M540,137 Q580,192 535,248 Q562,192 540,137 Z"/>
      <path d="M570,184 L582,198 L570,212 Z"/>

      <path d="M790,420 Q806,460 800,500" fill="none" stroke="var(--arrow)" stroke-width="8" stroke-linecap="round"/>
      <path d="M750,494 Q805,530 862,504 Q805,514 750,494 Z"/>
      <path d="M788,530 L802,543 L816,530 Z"/>

      <path d="M578,746 Q540,764 500,765" fill="none" stroke="var(--arrow)" stroke-width="8" stroke-linecap="round"/>
      <path d="M505,712 Q466,762 500,822 Q480,762 505,712 Z"/>
      <path d="M470,751 L457,765 L470,779 Z"/>

      <path d="M245,540 Q230,495 236,450" fill="none" stroke="var(--arrow)" stroke-width="8" stroke-linecap="round"/>
      <path d="M175,462 Q232,426 290,468 Q232,446 175,462 Z"/>
      <path d="M223,430 L237,416 L251,430 Z"/>
    </g>
  </svg>

  <h1 class="title">Analytical Cycle</h1>
  <p class="hub-label">Data</p>

  <p class="stage stage--measure">Higher quality Actions<br>yields improved Results<br>and <span class="key">Measure</span>ments</p>
  <p class="stage stage--inform">Accurate &amp; Relevant<br><span class="key">Inform</span>ation</p>
  <p class="stage stage--diagnose"><span class="key">Diagnose</span> an<br>opportunity to make<br>better Decisions</p>
  <p class="stage stage--action">Better Decisions<br>yield higher quality<br><span class="key">Actions</span></p>
</div>
</body>
</html>
```